Lumo-Vast.com -> We need someone to design a homepage [For Mobile]

We need a graphic design of our homepage for mobile, which will include login and signup. It's only the design we need, we would take care of the coding, so if you're a good designer you're welcome to participate. The Login & Registration page contain a few fields. Login --> Username & Password & Forgot my Password. Registration --> Email, Username, Password. Needs to be a clean design.[Registration in a different page, Login and Homepage in the same one]
Updates

Project Deadline Extended Reason: We're going to consider what we got so far and allow others to submit more designs as well, the final deadline would be this week, we won't extend it again. Added Saturday, December 20, 2014

Project Deadline Extended Reason: Very sorry, we just got more than expected designs and we want to go over all of them in order to make a proper decision - we would extend the project until the 1st of January 2015, this is definitely a FINAL date. Added Friday, December 26, 2014

Industry/Entity Type

Graphic Design

Number of Pages Required

2 page

Requirements
Must have
• * Enclosed our logo to include with the design.
• * Add the following text as well
• WANT TO EARN EXTRA MONEY?
• WITH LUMO-VAST.COM YOU CAN!
• LUMO-VAST.COM. IT'S AS EASY AS 1, 2, 3.
• (1) Register (2) Earn & Win Coins (3) Redeem Coins
• * It must have "Login" and "Register" buttons on the home page.
Nice to have
• [Note: Also to make it easier for you, enclosed a screenshot of the main page in a desktop (PC) view.]

```html
<!DOCTYPE html>
<html lang="en">
<head>
<meta charset="utf-8">
<title>Lumo-Vast.com – Mobile Home</title>
<link href="https://fonts.googleapis.com/css2?family=Open+Sans:wght@400;600;700&display=swap" rel="stylesheet">
<style>
  :root{
    --green:#4f9a1f;
    --green-dark:#3f8417;
    --green-text:#3c8a14;
    --band-grey:#e7e7e7;
    --dark-band:#7d7d7d;
    --yellow:#f3c52b;
    --yellow-dark:#e0ad12;
    --text:#555;
    --muted:#8a8a8a;
    --field-border:#c9c9c9;
    --social:#3d5a98;
    --footer:#3a3a3a;
    --white:#fff;
  }
  *{box-sizing:border-box;margin:0;padding:0}
  html,body{width:1200px;height:5341px;overflow:hidden;background:var(--white)}
  body{position:relative;font-family:"Open Sans",Arial,sans-serif;color:var(--text)}
  .abs{position:absolute;white-space:nowrap}
  .center{left:0;width:1200px;text-align:center}

  .site-header{left:0;top:0;width:1200px;height:207px;background:linear-gradient(#5aa626,var(--green-dark))}
  .brand{left:40px;top:38px;font-size:112px;font-weight:700;color:var(--white);line-height:1;letter-spacing:-2px}
  .brand-dot{left:604px;top:96px;width:32px;height:32px;border-radius:50%;background:var(--white)}
  .account-links{left:776px;top:86px;font-size:37px;line-height:52px;color:#1e3a0c;letter-spacing:-0.5px}

  .intro{top:246px;color:var(--green-text);font-weight:600}
  .intro-lead{font-size:42px;line-height:58px}
  .intro-sub{font-size:35px;line-height:52px}
  .video{left:50px;top:402px;width:1100px;height:620px;background:linear-gradient(#fbe6c3 0%,#f4d4a6 55%,#e28a3a 75%,#7fb9a8 100%)}
  .play{left:78px;top:431px;width:207px;height:135px;border-radius:22px;background:rgba(60,50,40,.75);border:4px solid rgba(255,255,255,.5)}

  .green-band{left:0;top:1086px;width:1200px;height:89px;background:linear-gradient(#3f8a17,#5aa626)}
  .section-title{left:0;width:1200px;text-align:center;font-size:42px;color:var(--green-text);background:var(--band-grey)}
  .activity-title{top:1175px;height:96px;line-height:96px}
  .activity-row{left:50px;width:1100px;height:100px}
  .avatar{left:0;top:0;width:100px;height:82px;background:#c4c4c4}
  .activity-text{left:128px;top:-8px;font-size:37px;line-height:50px;color:#666}
  .activity-time{right:0;top:34px;font-size:37px;color:var(--green-text)}
  .more-toggle{left:552px;top:1702px;width:96px;height:43px;background:#d8d8d8}

  .redeemed-title{top:1763px;height:114px;line-height:114px}
  .prize{top:1923px;height:232px}
  .prize-tag{font-size:30px;font-weight:700;color:#a9461b;background:var(--yellow);padding:4px 14px;line-height:40px}
  .claimed{top:2176px;color:var(--green-text)}
  .claimed-lead{font-size:44px;line-height:64px}
  .claimed-sub{font-size:36px;line-height:56px}

  .steps-title{left:0;top:2361px;width:1200px;height:114px;line-height:114px;text-align:center;background:var(--dark-band);color:#1f3a10;font-size:42px}
  .step-shape{left:310px;top:2535px}
  .step-text{left:370px;top:2776px;width:464px;text-align:center;color:var(--white);font-weight:600;white-space:normal}
  .step-name{font-size:44px;line-height:60px;margin-bottom:64px}
  .step-body{font-size:34px;line-height:52px}

  .partners-title{top:3390px;font-size:42px;color:#333}
  .partner{top:3500px;height:72px;border:3px solid #ccc;background:#f3f3f3}
  .join-title{top:3638px;font-size:42px;color:#333}
  .field{left:60px;width:1062px;height:89px;border:3px solid var(--field-border);border-radius:18px;padding-left:28px;font-size:36px;line-height:83px;color:#9a9a9a}
  .or{top:4158px;font-size:44px;color:#333}
  .social-btn{left:174px;top:4263px;width:848px;height:142px;border-radius:8px;background:linear-gradient(#4f6eab,var(--social))}
  .social-mark{left:28px;top:36px;width:70px;height:70px;background:var(--white);opacity:.9}
  .social-divider{left:178px;top:0;width:3px;height:142px;background:rgba(0,0,0,.25)}
  .social-label{left:210px;top:0;line-height:142px;font-size:52px;color:var(--white)}
  .join-btn{left:274px;top:4480px}

  .site-footer{left:0;top:4889px;width:1200px;height:452px;background:var(--footer)}
  .copyright{top:4940px;font-size:30px;line-height:44px;color:var(--white);font-weight:600}
  .footer-links{left:60px;top:5058px;width:1080px;text-align:center;font-size:29px;line-height:42px;color:#9a9a9a;white-space:normal}
</style>
</head>
<body>

<header class="abs site-header">
  <div class="abs brand">lumo-vast</div>
  <div class="abs brand-dot"></div>
  <div class="abs account-links">LOGIN<br>CREATE AN ACCOUNT</div>
</header>

<div class="abs center intro">
  <div class="intro-lead">WANT TO EARN EXTRA MONEY?</div>
  <div class="intro-sub">WITH LUMO-VAST.COM YOU CAN. SEE HOW IN 2 MINUTES!</div>
</div>

<div class="abs video" role="img" aria-label="Explainer video still: animated figures relaxing on a small island with palm trees"></div>
<div class="abs play">
  <svg width="200" height="128" viewBox="0 0 200 128"><polygon points="88,46 88,82 116,64" fill="#fff"/></svg>
</div>

<div class="abs green-band"></div>
<div class="abs section-title activity-title">RECENT MEMBER ACTIVITY</div>

<div class="abs activity-row" style="top:1305px">
  <div class="abs avatar"></div>
  <div class="abs activity-text">Fernwick, got the Total Coins In A Day<br>500 badge</div>
  <div class="abs activity-time">0 min ago</div>
</div>
<div class="abs activity-row" style="top:1447px">
  <div class="abs avatar"></div>
  <div class="abs activity-text">Fernwick, got the Total Coins In A Day<br>500 badge</div>
  <div class="abs activity-time">0 min ago</div>
</div>
<div class="abs activity-row" style="top:1590px">
  <div class="abs avatar"></div>
  <div class="abs activity-text">Fernwick, got the Total Coins In A Day<br>500 badge</div>
  <div class="abs activity-time">0 min ago</div>
</div>
<div class="abs more-toggle">
  <svg width="96" height="43" viewBox="0 0 96 43"><circle cx="48" cy="21" r="13" fill="none" stroke="#999" stroke-width="3"/><polyline points="41,18 48,25 55,18" fill="none" stroke="#999" stroke-width="3"/></svg>
</div>

<div class="abs section-title redeemed-title">RECENTLY REDEEMED</div>

<div class="abs prize" style="left:150px;width:230px" role="img" aria-label="Tablet computer"><div style="position:absolute;left:40px;top:0;width:170px;height:220px;background:linear-gradient(#333,#111);border-radius:14px;transform:rotate(-10deg)"></div></div>
<div class="abs prize-tag" style="left:140px;top:2080px">TABLET</div>
<div class="abs prize" style="left:490px;width:260px" role="img" aria-label="Gift card"><div style="position:absolute;left:20px;top:20px;width:230px;height:160px;background:linear-gradient(#2f7d5a,#175e3e);border-radius:10px;transform:rotate(-8deg)"></div></div>
<div class="abs prize-tag" style="left:490px;top:2070px">GIFT CARD</div>
<div class="abs prize" style="left:830px;width:230px" role="img" aria-label="E-reader device"><div style="position:absolute;left:20px;top:0;width:180px;height:220px;background:linear-gradient(#cfcfcf,#9c9c9c);border-radius:10px;transform:rotate(-6deg)"></div></div>
<div class="abs prize-tag" style="left:900px;top:2100px">E-READER</div>

<div class="abs center claimed">
  <div class="claimed-lead">OVER $250,000</div>
  <div class="claimed-sub">HAS BEEN CLAIMED BY OUR MEMBERS IN THE STORE</div>
</div>

<div class="abs steps-title">LUMO-VAST.COM. IT'S AS EASY AS 1, 2, 3.</div>

<svg class="abs step-shape" width="584" height="777" viewBox="0 0 584 777">
  <polygon points="0,220 150,107 434,107 584,220 584,660 292,777 0,660" fill="var(--yellow)"/>
  <circle cx="292" cy="100" r="108" fill="#e9e9e9"/>
  <circle cx="292" cy="100" r="96" fill="#fff"/>
  <text x="292" y="128" text-anchor="middle" font-family="Open Sans, sans-serif" font-size="76" font-weight="700" fill="var(--yellow-dark)">1</text>
</svg>
<div class="abs step-text">
  <div class="step-name">REGISTER</div>
  <div class="step-body">REGISTERING IS QUICK &amp; FREE! PLUS, YOU'LL GET BONUS COINS &amp; XP AS SOON AS YOU'VE JOINED.</div>
</div>
<svg class="abs" style="left:50px;top:2902px" width="75" height="107" viewBox="0 0 75 107"><rect width="75" height="107" fill="#888"/><polyline points="48,32 26,53 48,74" fill="none" stroke="#7bc043" stroke-width="10"/></svg>
<svg class="abs" style="left:1072px;top:2902px" width="75" height="107" viewBox="0 0 75 107"><rect width="75" height="107" fill="#888"/><polyline points="27,32 49,53 27,74" fill="none" stroke="#7bc043" stroke-width="10"/></svg>

<div class="abs center partners-title">OUR PARTNERS</div>
<svg class="abs" style="left:40px;top:3510px" width="36" height="52" viewBox="0 0 36 52"><polyline points="28,6 8,26 28,46" fill="none" stroke="var(--green)" stroke-width="8"/></svg>
<div class="abs partner" style="left:107px;width:285px"></div>
<div class="abs partner" style="left:417px;width:341px"></div>
<div class="abs partner" style="left:790px;width:282px"></div>
<svg class="abs" style="left:1110px;top:3510px" width="36" height="52" viewBox="0 0 36 52"><polyline points="8,6 28,26 8,46" fill="none" stroke="var(--green)" stroke-width="8"/></svg>

<div class="abs center join-title">JOIN THE LUMO-VAST COMMUNITY</div>
<div class="abs field" style="top:3746px">Enter your name</div>
<div class="abs field" style="top:3889px">Enter your email</div>
<div class="abs field" style="top:4031px">Enter your password</div>
<div class="abs center or">OR</div>

<div class="abs social-btn">
  <div class="abs social-mark"></div>
  <div class="abs social-divider"></div>
  <div class="abs social-label">Sign-up with Friendloop</div>
</div>

<svg class="abs join-btn" width="652" height="132" viewBox="0 0 652 132">
  <polygon points="0,0 590,0 652,66 590,132 0,132 52,66" fill="var(--yellow)"/>
  <text x="326" y="80" text-anchor="middle" font-family="Open Sans, sans-serif" font-size="40" font-weight="700" fill="#6a4a06">JOIN LUMO-VAST</text>
</svg>

<footer class="abs site-footer"></footer>
<div class="abs center copyright">Copyright © 2008 - 2014 Northbay Media Ltd | Paid Surveys by<br>Lumo-Vast.com - All Rights Reserved.</div>
<div class="abs footer-links">Privacy Policy | Special Terms &amp; Updates | About Us | Earnings Disclaimer | Blog | Contact Us<br>How it Works | Resources | how to make extra money | earn extra income from home | work from home | free money online | how to make money | paid surveys<br>ways to make money online | earn money | i need money | make money</div>

</body>
</html>
```